Harbinger Cargo needs a business card design.

Design a double-sided business card for new freight business. On the front, would like to see our logo along with the following info:

Malcolm Strathby
CEO/FOUNDER
555-207-4163
malcolmstrathby@harbinger-cargo.example

On the reverse side, we would like to use the graphic image of our logo only without the Harbinger Cargo name.

```html
<!DOCTYPE html>
<html lang="en">
<head>
<meta charset="utf-8">
<title>Harbinger Cargo — Business Card</title>
<link href="https://fonts.googleapis.com/css2?family=Montserrat:wght@700;800&family=Open+Sans:wght@400;600&display=swap" rel="stylesheet">
<style>
  :root {
    --navy: #1c1a55;
    --red: #b8202a;
    --ink: #3a3a44;
    --paper: #ffffff;
    --backdrop: #d9d9dc;
  }
  * { margin: 0; padding: 0; box-sizing: border-box; }
  html, body { width: 1200px; height: 901px; overflow: hidden; background: var(--backdrop); }
  .stage {
    width: 1200px; height: 901px;
    display: flex; align-items: center; justify-content: center; gap: 40px;
  }
  .card {
    position: relative;
    width: 540px; height: 309px;
    box-shadow: 0 10px 28px rgba(0,0,0,.25);
    overflow: hidden;
  }
  .card--back { background: var(--navy); }
  .card--front { background: var(--paper); }
  .front-logo {
    position: absolute; left: 36px; top: 136px;
    display: flex; align-items: center; gap: 10px;
  }
  .front-logo .mark-dot { width: 14px; height: 14px; background: var(--red); border-radius: 50%; flex: none; }
  .front-logo .wordmark {
    font-family: "Montserrat", sans-serif;
    font-weight: 800;
    font-size: 18px;
    line-height: 1.05;
    letter-spacing: 2px;
    text-transform: uppercase;
    color: var(--navy);
  }
  .divider {
    position: absolute; left: 248px; top: 80px;
    width: 1.5px; height: 140px; background: var(--navy);
  }
  .details { position: absolute; left: 266px; top: 82px; }
  .person-name {
    font-family: "Montserrat", sans-serif; font-weight: 800; font-size: 19px;
    color: var(--navy); line-height: 1.1;
  }
  .person-name .surname { color: var(--red); }
  .person-title {
    font-family: "Open Sans", sans-serif; font-size: 11.5px; color: var(--ink);
    letter-spacing: .3px; margin-top: 3px; margin-bottom: 14px;
  }
  .contact-list { list-style: none; font-family: "Open Sans", sans-serif; font-size: 10.5px; color: var(--ink); }
  .contact-list li { display: flex; align-items: center; gap: 7px; margin-bottom: 5px; white-space: nowrap; }
  .contact-list svg { width: 10px; height: 10px; flex: none; fill: var(--red); }
  .edge-bands { position: absolute; left: 0; bottom: 0; width: 540px; height: 60px; }
</style>
</head>
<body>
<main class="stage">
  <section class="card card--back" aria-label="Card reverse"></section>

  <section class="card card--front" aria-label="Card front">
    <div class="front-logo">
      <span class="mark-dot"></span>
      <span class="wordmark">Harbinger<br>Cargo</span>
    </div>
    <div class="divider"></div>
    <div class="details">
      <p class="person-name">Malcolm <span class="surname">Strathby</span></p>
      <p class="person-title">CEO/FOUNDER</p>
      <ul class="contact-list">
        <li>
          <svg viewBox="0 0 10 10"><path d="M2 0.5 L3.6 0.5 L4.2 2.8 L3.1 3.6 Q4 5.8 6.3 6.9 L7.1 5.8 L9.5 6.4 L9.5 8 Q9.5 9.5 8 9.5 Q0.5 9 0.5 2 Q0.5 0.5 2 0.5Z"/></svg>
          555-207-4163
        </li>
        <li>
          <svg viewBox="0 0 10 10"><path d="M0.5 2 H9.5 V8.5 H0.5Z M0.5 2 L5 5.5 L9.5 2" fill="var(--red)" stroke="#fff" stroke-width=".7"/></svg>
          malcolmstrathby@harbinger-cargo.example
        </li>
        <li>
          <svg viewBox="0 0 10 10"><circle cx="5" cy="5" r="4.5"/><path d="M0.5 5 H9.5 M5 0.5 Q2.5 5 5 9.5 M5 0.5 Q7.5 5 5 9.5" stroke="#fff" stroke-width=".6" fill="none"/></svg>
          www.harbinger-cargo.example
        </li>
      </ul>
    </div>
    <svg class="edge-bands" viewBox="0 0 540 60" preserveAspectRatio="none" aria-hidden="true">
      <polygon points="0,53 330,53 338,40 343,40 333,60 0,60" fill="var(--navy)"/>
      <polygon points="345,40 540,40 540,44 352,44 343,60 340,60" fill="var(--red)"/>
    </svg>
  </section>
</main>
</body>
</html>
```